Card for invoking rights with police

Our criminal defense law firm is seeking proposals for a design for our card intended for clients to carry with them in their car. Upon being pulled over, they would hand this card to the officer.
Text for the back of the card:
"For Law Enforcement:"
"I will comply with lawful orders but respectfully decline any test or other requests without my attorney. I wish to remain silent, do not consent to searches, and request to speak with my attorney now.
The back of the card should prominently feature the text and the firm logo should be secondary.
Front
Must prominently feature contact info: 503-555-0182. Do not include attorney name, email, phone from the example file. This is intended to be generic for the firm and not tied to an individual lawyer.
Included for design reference: current business card, firm logo.
We intend to use trenvo.com to produce the cards.
Updates
The back of the card should prominently display the text regarding invocation of rights. Please title it "For Law Enforcement".
Target Market(s)
People who have been stopped by police
Contact Information for Business Card
see project description
Look and feel

```html
<!DOCTYPE html>
<html lang="en">
<head>
<meta charset="utf-8">
<title>Halvern Law Firm – Rights Card</title>
<link href="https://fonts.googleapis.com/css2?family=Tinos:wght@400;700&display=swap" rel="stylesheet">
<style>
  :root {
    --backdrop: #2a2a2c;
    --card: #f7f7f5;
    --navy: #123c63;
    --ink: #4a4a4a;
    --white: #ffffff;
  }
  * { margin: 0; padding: 0; box-sizing: border-box; }
  html, body {
    width: 1200px;
    height: 782px;
    overflow: hidden;
    background: var(--backdrop);
    font-family: "Tinos", "Times New Roman", serif;
  }
  .sheet {
    width: 1200px;
    height: 782px;
    display: flex;
    align-items: center;
    justify-content: center;
    gap: 60px;
  }
  .card {
    position: relative;
    width: 520px;
    height: 297px;
    background: var(--card);
    box-shadow: 0 10px 30px rgba(0,0,0,0.35);
    overflow: hidden;
  }

  /* Front */
  .brand {
    position: absolute;
    top: 92px;
    left: 0;
    right: 0;
    display: flex;
    align-items: center;
    justify-content: center;
    gap: 14px;
  }
  .brand-square {
    width: 30px;
    height: 30px;
    background: var(--navy);
  }
  .brand-name {
    color: var(--navy);
    font-size: 26px;
    font-weight: 400;
    letter-spacing: 0.22em;
  }
  .front .band {
    position: absolute;
    left: 0;
    right: 0;
    top: 186px;
    height: 34px;
    background: var(--navy);
    display: flex;
    align-items: center;
    justify-content: center;
  }
  .phone {
    color: var(--white);
    font-size: 15px;
    letter-spacing: 0.25em;
  }

  /* Back */
  .notice {
    position: absolute;
    top: 58px;
    left: 46px;
    right: 46px;
    text-align: center;
  }
  .notice-title {
    color: var(--navy);
    font-size: 15px;
    font-weight: 700;
    letter-spacing: 0.02em;
    margin-bottom: 8px;
  }
  .notice-body {
    color: var(--ink);
    font-size: 15px;
    line-height: 1.3;
  }
  .back .band {
    position: absolute;
    left: 0;
    right: 0;
    top: 232px;
    height: 30px;
    background: var(--navy);
    display: flex;
    align-items: center;
    padding-left: 56px;
  }
  .band-mark {
    position: absolute;
    left: 18px;
    top: 8px;
    width: 14px;
    height: 14px;
    background: var(--white);
  }
  .web {
    color: var(--white);
    font-size: 13px;
    letter-spacing: 0.32em;
  }
</style>
</head>
<body>
  <main class="sheet">
    <section class="card front" aria-label="Card front">
      <div class="brand">
        <span class="brand-square"></span>
        <span class="brand-name">HALVERN LAW FIRM</span>
      </div>
      <div class="band">
        <span class="phone">503-555-0182</span>
      </div>
    </section>

    <section class="card back" aria-label="Card back">
      <div class="notice">
        <h1 class="notice-title">FOR LAW ENFORCEMENT</h1>
        <p class="notice-body">I will comply with lawful orders but respectfully decline any test or other requests without my attorney. I wish to remain silent, do not consent to searches, and request to speak with my attorney now.</p>
      </div>
      <div class="band">
        <span class="band-mark"></span>
        <span class="web">www.halvernlawfirm.com</span>
      </div>
    </section>
  </main>
</body>
</html>
```